Flyer Rework for Accountants and Lawyers

Information flyer for accountants and lawyers. Text and flowchart provided. Just need to make it look presentable for print and email. Needs to add logo (AI file provided) and provide graphics. No more than two pages. Our corporate visual identify guidelines are attached (MUST Use). Completed on both AI file and PPTX file.
Target Market(s)
Accountants, Company Directors and Lawyers
Industry/Entity Type
Finance And Accounting
Requirements
Must have
- Our corporate visual identify guidelines are attached (MUST Use)

```html
<!DOCTYPE html>
<html lang="en">
<head>
<meta charset="utf-8">
<title>Fairbank Advisory – Director Penalty Notice Flyer</title>
<link href="https://fonts.googleapis.com/css2?family=Montserrat:wght@500;600;700&family=Arimo:wght@400;700&display=swap" rel="stylesheet">
<style>
:root{
  --green:#6cbf45;
  --blue:#5cc3dd;
  --dark:#4a4a4a;
  --grey:#77777b;
  --grey-light:#ececec;
  --grey-mid:#d9d9d9;
  --navy:#1e2a5e;
  --ink:#333;
  --paper:#ffffff;
  --bg:#f4f4f4;
}
*{box-sizing:border-box;margin:0;padding:0}
html,body{width:800px;height:1200px;overflow:hidden;background:var(--bg)}
body{position:relative;font-family:"Arimo",Arial,sans-serif;color:var(--ink)}
.page{position:absolute;top:345px;width:360px;height:510px;background:var(--paper);overflow:hidden;box-shadow:0 3px 10px rgba(0,0,0,.18)}
.cover{left:30px}
.info{left:410px}

/* cover */
.cover-shapes{position:absolute;inset:0}
.brand{position:absolute;left:18px;top:30px}
.brand-name{font-family:"Montserrat",sans-serif;font-weight:600;font-size:10px;color:var(--green);letter-spacing:.2px}
.brand-sub{font-size:4.8px;color:var(--grey);margin-top:2px}
.photo{position:absolute;left:0;top:83px;width:304px;height:267px;background:linear-gradient(135deg,#7a6a55 0%,#b79a7e 35%,#3e3a36 65%,#8f8a80 100%)}
.slogan{position:absolute;left:20px;top:389px;font-family:"Montserrat",sans-serif;font-weight:700;font-size:20px;line-height:20px;letter-spacing:.3px}
.slogan .g{color:var(--green)}
.slogan .b{color:var(--blue)}
.slogan .d{color:var(--dark)}
.cover-intro{position:absolute;left:20px;top:455px;width:195px;font-size:5.6px;line-height:7px;font-weight:700;color:var(--dark)}
.cover-url{position:absolute;right:16px;top:488px;font-size:8px;font-weight:700;color:#fff}

/* info page */
.info h2{position:absolute;left:16px;font-size:6.5px;font-weight:700;color:var(--green)}
.para{position:absolute;left:16px;width:328px;font-size:4.4px;line-height:5.6px;color:var(--ink)}
.facts{position:absolute;left:16px;top:60px;width:327px;border-collapse:collapse;font-size:4.4px;line-height:5.6px}
.facts th{background:var(--green);color:var(--ink);font-weight:700;height:9px;padding:0 3px;border:1px solid #fff}
.facts td{padding:2px 5px;border:1px solid #fff;vertical-align:middle}
.facts tr:nth-child(odd) td{background:var(--grey-light)}
.facts tr:nth-child(even) td{background:var(--grey-mid)}
.facts td:first-child{width:78px}
.facts ul{padding-left:9px}
.tips{position:absolute;left:16px;top:230px;width:327px;display:grid;grid-template-columns:1fr 1fr;column-gap:18px;font-size:4.4px;line-height:5.6px}
.tips ul{padding-left:9px}
.tips li{margin-bottom:6px}
.flow-lines{position:absolute;inset:0;pointer-events:none}
.node{position:absolute;background:var(--blue);color:#fff;font-size:4.4px;line-height:5.4px;padding:4px 5px}
.flag{position:absolute;font-size:5px;font-weight:700;color:var(--ink)}
.footer{position:absolute;left:0;bottom:0;width:100%;height:19px;background:var(--navy);border-top:2px solid var(--blue);color:#fff;font-size:5.3px;line-height:6.4px;text-align:center;padding-top:2px}
</style>
</head>
<body>

<section class="page cover">
  <svg class="cover-shapes" width="360" height="510" viewBox="0 0 360 510" aria-hidden="true">
    <polygon points="262,0 360,0 360,372 300,356 262,356" fill="var(--grey)"/>
    <rect x="0" y="77" width="262" height="2.5" fill="var(--green)"/>
    <polygon points="0,356 300,356 360,372 360,378 300,362 0,362" fill="var(--green)"/>
    <polygon points="330,510 360,440 360,510" fill="var(--green)"/>
    <polygon points="120,510 360,428 360,510" fill="var(--blue)"/>
  </svg>
  <div class="brand">
    <div class="brand-name">FAIRBANK ADVISORY</div>
    <div class="brand-sub">Restructuring &amp; Solvency Accountants</div>
  </div>
  <div class="photo" role="img" aria-label="Photo of two smiling professional women applauding in a meeting"></div>
  <div class="slogan">
    <div class="g">INDEPENDENT</div>
    <div class="b">CONCISE</div>
    <div class="d">EFFICIENT</div>
  </div>
  <p class="cover-intro">Company directors and their advisors need to be aware that non-lodgement of Business Activities Statements (“BAS”) and Superannuation Guarantee Charge (“SCG”) Statements with the ATO may be personally liability for these debts.</p>
  <div class="cover-url">www.fairbankadvisory.example</div>
</section>

<section class="page info">
  <h2 style="top:12px">Director Penalty Notices (“DPN”)</h2>
  <p class="para" style="top:25px">The ATO uses DPNs and Garnishee Notices to recovery tax debts and to impose positive obligations on Directors to deal with outstanding PAYG Withholding and the Superannuation Guarantee Charge debts (“Tax Debts”). The DPN regime makes directors of companies who fail to pay Tax Debts personally liable. The key facts of DPN regime are outlined below:</p>

  <table class="facts">
    <tr><th>Facts</th><th>Key facts of a Directors Penalty Notice</th></tr>
    <tr style="height:15px"><td>Director personal liabilities</td><td>Directors become personally liable for Tax Debts 21 days are the DPN Notice is issued</td></tr>
    <tr style="height:23px"><td>Automatic liability for unreported and unpaid Tax Debts</td><td>Where a company’s Tax Debts were both unreported and unpaid 3 months after the due date, the directors are automatically personally liable for the Tax Debts.</td></tr>
    <tr style="height:43px"><td>Avoiding personal liability for directors once they receive a DPN</td><td>Within 21 days of issuing the DPN (which may be received a week or more after issue), a director can avoid personal liability by either:
      <ul><li>Paying the Tax Debt.</li><li>Appointing an Administrator to the company.</li><li>Appointing a Liquidator to the company.</li></ul></td></tr>
    <tr style="height:24px"><td>Effect on new directors</td><td>New directors are liable if outstanding Tax Debts are unpaid 30 days after their appointment as director</td></tr>
    <tr style="height:21px"><td>Time frames</td><td>ATO can only enforce a DPN after 21 days of giving notice to the director and notice can be given to the company tax agent</td></tr>
  </table>

  <h2 style="top:217px">Tips for directors to limit or avoid personal liability:</h2>
  <div class="tips">
    <ul>
      <li>Always lodge BAS and SGC Statements within 3 months of the due date, even if the liability cannot be paid</li>
      <li>Seek professional advice from an insolvency practitioner about the options available and possibly save the company through a financial restructure.</li>
    </ul>
    <ul>
      <li>Act immediately upon receipt of a DPN and consider a payment arrangement with the ATO. This should be considered with care as payments made can be considered as preference payments to the ATO. If a liquidator is appointed. The ATO can make the directors personally liable for the ATO preference claim</li>
    </ul>
  </div>

  <h2 style="top:287px">How Fairbank Advisory can help?</h2>
  <p class="para" style="top:300px">Fairbank Advisory is a firm that specialises in insolvency and restructuring, we are here to assist your clients who experiencing financial difficulties with straight forward solutions in simple to understand terms. The initial consultation is free, strictly confidential and without obligation.</p>

  <h2 style="top:342px">Summary of the DPN</h2>
  <svg class="flow-lines" width="360" height="510" viewBox="0 0 360 510" aria-hidden="true">
    <g fill="none" stroke="#444" stroke-width=".8">
      <path d="M68 405 H76"/>
      <path d="M100 383 V366 Q100 360 106 360 H141"/>
      <path d="M100 430 V440 Q100 446 106 446 H141"/>
      <path d="M175 350 V346 Q175 340 181 340 H284 Q290 340 290 346 V350"/>
      <path d="M270 386 V396 Q270 402 264 402 H191 Q185 402 185 408 V424"/>
      <path d="M330 386 V434 Q330 440 324 440 H292"/>
    </g>
  </svg>
  <div class="node" style="left:16px;top:378px;width:52px;height:54px">Issued Director’s Penalty Notice By ATO</div>
  <div class="node" style="left:76px;top:383px;width:48px;height:47px">Business Activity Statement and Superannuation Guarantee Charge lodged</div>
  <div class="node" style="left:141px;top:350px;width:59px;height:53px">Director not personally liable yet (Have options) (RIGHTS PRESERVED)</div>
  <div class="node" style="left:141px;top:424px;width:51px;height:44px">Director Automatically personally liable</div>
  <div class="node" style="left:239px;top:350px;width:104px;height:36px">If Directors act within 21 days and:<br>1.Wind up Company voluntarily, or<br>2.Appoint Voluntary Administrator, or<br>3.Pay debt in full</div>
  <div class="node" style="left:239px;top:424px;width:53px;height:44px">Director not personally liable but the company is still insolvent</div>
  <span class="flag" style="left:118px;top:354px">NO</span>
  <span class="flag" style="left:118px;top:440px">YES</span>
  <span class="flag" style="left:210px;top:396px">NO</span>
  <span class="flag" style="left:297px;top:420px">YES</span>

  <div class="footer">Please call (02) 5550 1234 to speak to one of our solvency specialist<br>or email info@fairbankadvisory.example.</div>
</section>

</body>
</html>
```